integrative health clinic-Medical massage, acupuncture, chiropractic

we like our logo, but are open to new ideas. We need a new card design. We have added chiropractic and acupuncture that we have put under the name of the business. We are an integrative medical clinic

Target Market(s)

General public, athletes

Contact Information for Business Card

Phone 5055582917
Fax 5055582916
Hours Monday-Friday 9-6
Saturday 10-6
The 20% can be smaller on the back

Colors
3176b5
0355a3

Requirements
Must have
• Logo but am open to ideas
Nice to have
• We are an integrated medical clinic but also want to be personable. We want the card fun and inviting

```html
<!DOCTYPE html>
<html lang="en">
<head>
<meta charset="utf-8">
<title>Clear River Wellness — Business Card</title>
<link href="https://fonts.googleapis.com/css2?family=Open+Sans:wght@400;600;700&display=swap" rel="stylesheet">
<style>
  :root {
    --blue-light: #3176b5;
    --blue-deep: #0355a3;
    --blue-bright: #1a8fd6;
    --ink: #1b2430;
    --white: #ffffff;
    --grey: #7d7f86;
    --stage: #8b8e97;
  }
  * { box-sizing: border-box; margin: 0; padding: 0; }
  html, body { width: 1200px; height: 945px; overflow: hidden; }
  body {
    background: var(--stage);
    font-family: "Open Sans", Arial, sans-serif;
    color: var(--white);
    position: relative;
  }
  .card {
    position: absolute;
    top: 158px;
    width: 360px;
    height: 630px;
    border-radius: 26px;
    overflow: hidden;
    background: linear-gradient(160deg, var(--blue-deep) 0%, var(--blue-light) 55%, #0f7fc0 100%);
  }
  .card--back { left: 170px; text-align: center; }
  .card--front { left: 670px; }

  .brand { display: flex; flex-direction: column; align-items: center; }
  .brand__row { display: flex; align-items: center; gap: 8px; }
  .brand__dot { width: 14px; height: 14px; border-radius: 50%; background: currentColor; }
  .brand__name { font-size: 28px; font-weight: 600; letter-spacing: -0.5px; line-height: 1; }
  .brand__tagline { font-size: 11px; margin-top: 5px; letter-spacing: .3px; }

  .card--back .brand { margin-top: 92px; }
  .book-online { margin: 34px auto 0; width: 110px; height: 62px; display: block; }
  .site { font-size: 17px; font-weight: 600; margin-top: 22px; }
  .insurance { font-size: 19px; font-weight: 600; line-height: 1.3; margin-top: 70px; padding: 0 22px; }
  .divider { width: 250px; height: 1px; margin: 14px auto 12px; background: linear-gradient(90deg, transparent, var(--white), transparent); }
  .offer { font-size: 22px; font-weight: 600; letter-spacing: .5px; }

  .front-art { position: absolute; inset: 0; width: 360px; height: 630px; }
  .card--front .brand { position: absolute; top: 70px; left: 0; right: 0; color: var(--ink); }
  .notch { position: absolute; left: -6px; top: 290px; width: 54px; height: 54px; background: var(--white); border-radius: 8px; }
  .front-text { position: absolute; left: 62px; right: 18px; top: 262px; }
  .specialty { font-size: 16px; font-weight: 600; line-height: 1.3; }
  .address { font-size: 16px; font-weight: 600; line-height: 1.2; margin-top: 10px; }
  .contacts { list-style: none; margin-top: 10px; position: relative; }
  .contacts::before { content: ""; position: absolute; left: -16px; top: -20px; bottom: 8px; width: 2px; background: var(--white); }
  .contacts li { font-size: 15.5px; font-weight: 600; line-height: 1.25; position: relative; }
  .contacts li::before { content: ""; position: absolute; left: -21px; top: 6px; width: 12px; height: 12px; border-radius: 50%; background: var(--white); }
  .hours__title { font-size: 18px; font-weight: 600; margin-top: 12px; display: inline-block; border-bottom: 2px solid var(--blue-bright); }
  .hours__table { font-size: 11px; margin-top: 6px; line-height: 1.4; }
  .hours__table td { padding-right: 6px; }
</style>
</head>
<body>

  <section class="card card--back" aria-label="Card back">
    <div class="brand">
      <div class="brand__row"><span class="brand__dot"></span><span class="brand__name">Clear River Wellness</span></div>
      <span class="brand__tagline">Sports Therapy and Wellness Center</span>
    </div>
    <svg class="book-online" viewBox="0 0 110 62" aria-label="Book Online">
      <polygon points="0,6 110,0 58,62" fill="var(--white)"/>
      <text x="52" y="22" text-anchor="middle" font-size="12" font-weight="700" fill="var(--blue-deep)" font-family="Open Sans, sans-serif">Book</text>
      <text x="56" y="35" text-anchor="middle" font-size="12" font-weight="700" fill="var(--blue-deep)" font-family="Open Sans, sans-serif">Online</text>
    </svg>
    <p class="site">www.clearriverwellness.com</p>
    <p class="insurance">We accept some insurance, workers Comp and Personal Injury</p>
    <div class="divider"></div>
    <p class="offer">20% OFF FIRST VISIT</p>
  </section>

  <section class="card card--front" aria-label="Card front">
    <svg class="front-art" viewBox="0 0 360 630" aria-hidden="true">
      <polygon points="0,0 360,0 360,150 180,230 0,150" fill="var(--white)"/>
      <polygon points="70,60 140,30 180,70" fill="var(--blue-deep)"/>
      <polygon points="0,150 180,230 360,150 360,175 180,250 0,175" fill="var(--grey)" opacity=".85"/>
      <polygon points="0,175 180,250 360,175 360,190 180,262 0,190" fill="var(--white)"/>
    </svg>
    <div class="brand">
      <div class="brand__row"><span class="brand__dot"></span><span class="brand__name">Clear River Wellness</span></div>
      <span class="brand__tagline">Sports Therapy and Wellness Center</span>
    </div>
    <div class="notch"></div>
    <div class="front-text">
      <p class="specialty">Specializing in Medical Sports massage and Manual Therapies.</p>
      <p class="address">418 Alder Lane, Suite 2<br>Riverton, NM 87000</p>
      <ul class="contacts">
        <li>5055582917</li>
        <li>5055582916</li>
        <li>hello@clearriverwellness.com</li>
        <li>www.clearriverwellness.com</li>
      </ul>
      <p class="hours__title">Hours</p>
      <table class="hours__table">
        <tr><td>Monday to Friday</td><td>:09:00 A.M. – 6:00 P.M.</td></tr>
        <tr><td>Saturday</td><td>:10:00 A.M. – 6:00 P.M.</td></tr>
      </table>
    </div>
  </section>

</body>
</html>
```